Walk Bright through the Seasons: 52 Weeks to a Year of Courage and Calm

This is a non-fiction, self-help book. The first edition was published a decade ago, and it needs a new design. Nothing too literal (no actual hearts on the cover) but something inspirational or perhaps something quite plain. The current cover is below for reference, but I DO NOT want something similar to that. It is outdated.

The cover must include:

1. Title: Walk Bright through the Seasons
2. Subtitle: 52 Weeks to a Year of Courage and Calm
3. Author Name: Tobin Wells

It should also have plenty of "white space" in other words the fonts shouldnt be so big that they take up the whole cover.

Dimensions: 9" x 6.25"

Target Market(s)

adults interested in personal development

Font styles to use
Serif
Script

Colors

Designer to choose colors to be used in the design.

Requirements
Must have
• Classic look and feel. The current design is too busy. I have included examples of the style I like below. I'm open to a singular graphic/photo but nothing more than that. Probably plain text is best.
• Please look at the samples I have included of best-selling books in the genre that I like. The cover should be modeled after these.

```html
<!DOCTYPE html>
<html lang="en">
<head>
<meta charset="utf-8">
<title>Walk Bright through the Seasons — Book Cover</title>
<link rel="stylesheet" href="https://fonts.googleapis.com/css2?family=Cormorant+Garamond:wght@500&family=Pinyon+Script&display=swap">
<style>
  :root {
    --stage: #c9d0d2;
    --cover-blue: #0595d3;
    --cover-blue-light: #2aa6dd;
    --ink: #ffffff;
    --leaf: rgba(255, 255, 255, 0.55);
  }
  * { margin: 0; padding: 0; box-sizing: border-box; }
  html, body {
    width: 1200px;
    height: 800px;
    overflow: hidden;
    background: var(--stage);
  }
  .stage {
    width: 1200px;
    height: 800px;
    display: flex;
    align-items: center;
    justify-content: center;
  }
  .cover {
    position: relative;
    width: 520px;
    height: 749px;
    background: linear-gradient(160deg, var(--cover-blue-light) 0%, var(--cover-blue) 35%, var(--cover-blue) 100%);
    color: var(--ink);
    overflow: hidden;
  }
  .author {
    position: absolute;
    top: 62px;
    left: 0;
    right: 0;
    text-align: center;
    font-family: "Cormorant Garamond", Georgia, serif;
    font-weight: 500;
    font-size: 29px;
    letter-spacing: 0.14em;
    text-transform: uppercase;
  }
  .title {
    position: absolute;
    top: 160px;
    left: 0;
    right: 0;
    height: 360px;
    font-family: "Pinyon Script", cursive;
    font-weight: 400;
  }
  .title-line {
    position: absolute;
    display: block;
    white-space: nowrap;
    line-height: 1;
  }
  .title-line--first {
    top: 40px;
    left: 40px;
    font-size: 86px;
  }
  .title-line--joiner {
    top: 148px;
    left: 190px;
    font-size: 40px;
    transform: rotate(-6deg);
  }
  .title-line--last {
    top: 200px;
    left: 70px;
    font-size: 100px;
  }
  .leaf {
    position: absolute;
    display: block;
  }
  .leaf--upper { top: 10px; left: 228px; width: 82px; height: 56px; }
  .leaf--lower { top: 160px; left: 330px; width: 82px; height: 56px; }
  .subtitle {
    position: absolute;
    top: 620px;
    left: 0;
    right: 0;
    text-align: center;
    font-family: "Cormorant Garamond", Georgia, serif;
    font-weight: 500;
    font-size: 24px;
    line-height: 1.3;
    letter-spacing: 0.1em;
    text-transform: uppercase;
  }
</style>
</head>
<body>
  <main class="stage">
    <article class="cover">
      <p class="author">Tobin Wells</p>

      <h1 class="title">
        <svg class="leaf leaf--upper" viewBox="0 0 82 56" role="img" aria-label="Small palm frond ornament">
          <ellipse cx="41" cy="28" rx="39" ry="18" transform="rotate(-18 41 28)" fill="var(--leaf)"/>
        </svg>
        <span class="title-line title-line--first">Walk Bright</span>
        <span class="title-line title-line--joiner">through the</span>
        <svg class="leaf leaf--lower" viewBox="0 0 82 56" role="img" aria-label="Small palm frond ornament">
          <ellipse cx="41" cy="28" rx="39" ry="18" transform="rotate(-18 41 28)" fill="var(--leaf)"/>
        </svg>
        <span class="title-line title-line--last">Seasons</span>
      </h1>

      <p class="subtitle">52 Weeks to a Year of<br>Courage and Calm</p>
    </article>
  </main>
</body>
</html>
```